Cover design for new academic journal on deconstruction and psychoanalysis

We need a cover for a new academic journal on deconstruction and psychoanalysis. The name of the journal is "The Suspended Threshold: A Journal of Deconstruction and Psychoanalysis" (ST) and it is published by the Halvern College Press(HCP).

Here is a description of the journal on the HCP website:

http://www.halvernpress.example.edu/product/The-Suspended-Threshold,318264.aspx

We are looking for a design that is more abstract and does not have icons or photographs of people, especially not photos of Kovalt or Brisk. The design should be contemporary with clean lines and simple fonts. Again, it should be abstract, with no icons or iconography.

The cover should simply have the full name of the journal and then "Volume 1, Issue 1, 2014" on the cover and "Vol. 1, No. 1, 2014" on the spine.

Attached you can see some ideas that we rejected from HCP. It is important that you understand that these designs were rejected and are just being offered as examples of what the cover will look like in general, as a template of sorts.

The cover should have a bold abstract design, with a space for the title and "Volume 1, Issue 1, 2014."

Something bold and contemporary.

Target Market(s)

Academics, scholars and psychoanalysts.

Industry/Entity Type

University

Font styles to use
Sans Serif

Requirements
Must have
• Must be abstract, bold, have color, and must be contemporary.
Should not have
• No icons, no photographs of Kovalt, Brisk, or anyone.

```html
<!DOCTYPE html>
<html lang="en">
<head>
<meta charset="utf-8">
<title>The Suspended Threshold — Volume 1, Issue 1, 2014</title>
<link rel="stylesheet" href="https://fonts.googleapis.com/css2?family=Bebas+Neue&family=Libre+Baskerville:ital@0;1&display=swap">
<style>
  :root {
    --paper: #ffffff;
    --frame-line: #9a9a9a;
    --maroon-deep: #260303;
    --maroon: #4c0707;
    --ember: #c8170e;
    --glow: #ff3b22;
    --hot: #ff7a5c;
    --ink-light: #ffffff;
  }
  html, body {
    margin: 0;
    padding: 0;
    width: 875px;
    height: 1200px;
    overflow: hidden;
    background: var(--paper);
  }
  .cover {
    position: relative;
    width: 875px;
    height: 1200px;
    box-sizing: border-box;
    border: 2px solid var(--frame-line);
    background: var(--paper);
  }
  .cover__art {
    position: absolute;
    left: 29px;
    top: 29px;
    width: 817px;
    height: 1137px;
    background:
      radial-gradient(ellipse 30% 18% at 62% 14%, rgba(255, 122, 92, 0.55), transparent 70%),
      radial-gradient(ellipse 60% 35% at 60% 20%, rgba(255, 59, 34, 0.85), transparent 72%),
      radial-gradient(ellipse 35% 22% at 20% 16%, rgba(255, 59, 34, 0.70), transparent 72%),
      radial-gradient(ellipse 45% 40% at 85% 48%, rgba(255, 59, 34, 0.75), transparent 72%),
      radial-gradient(ellipse 40% 40% at 78% 82%, rgba(200, 23, 14, 0.85), transparent 72%),
      radial-gradient(ellipse 30% 25% at 45% 62%, rgba(200, 23, 14, 0.55), transparent 72%),
      linear-gradient(120deg, var(--maroon-deep) 0%, var(--maroon) 35%, #8a0d08 70%, var(--ember) 100%);
  }
  .masthead {
    position: absolute;
    left: 78px;
    top: 672px;
    color: var(--ink-light);
  }
  .masthead__title {
    margin: 0;
    font-family: "Bebas Neue", "Oswald", sans-serif;
    font-weight: 400;
    font-size: 88px;
    line-height: 72px;
    letter-spacing: 0.5px;
  }
  .masthead__title span { display: block; }
  .masthead__subtitle {
    margin: 8px 0 0 -3px;
    font-family: "Libre Baskerville", Georgia, serif;
    font-style: italic;
    font-size: 27px;
    line-height: 40px;
  }
  .masthead__subtitle span { display: block; }
  .issue-line {
    position: absolute;
    left: 75px;
    top: 1076px;
    margin: 0;
    color: var(--ink-light);
    font-family: "Libre Baskerville", Georgia, serif;
    font-size: 21px;
  }
</style>
</head>
<body>
  <main class="cover">
    <div class="cover__art" role="img" aria-label="Bold abstract long-exposure photograph of bright red light trails falling diagonally across a dark maroon background"></div>
    <header class="masthead">
      <h1 class="masthead__title">
        <span>The</span>
        <span>Suspended</span>
        <span>Threshold</span>
      </h1>
      <p class="masthead__subtitle">
        <span>A Journal of</span>
        <span>Deconstruction and</span>
        <span>Psychoanalysis</span>
      </p>
    </header>
    <p class="issue-line">Volume 1, Issue 1, 2014</p>
  </main>
</body>
</html>
```